Need new label for my eczema cream. The Pine Grove Soothed My Skin. PLS NOTHING LAME AND CLIP ART-ISH!

Think corvanta website meets eczema....our site is pinegrovesoothe.com ill attach our current logo.

```html
<!DOCTYPE html>
<html lang="en">
<head>
<meta charset="utf-8">
<title>Soothing Cream Label – Front Side</title>
<link href="https://fonts.googleapis.com/css2?family=Montserrat:wght@400;500;800&display=swap" rel="stylesheet">
<style>
  :root {
    --page: #f5f5f5;
    --sky: #b9e2ea;
    --foam: #ffffff;
    --sand: #feedd3;
    --ink: #1c1450;
    --icon-tint: #ddd6e8;
  }
  html, body {
    margin: 0;
    padding: 0;
    width: 857px;
    height: 1200px;
    overflow: hidden;
    background: var(--page);
    font-family: "Montserrat", sans-serif;
    color: var(--ink);
  }
  .label {
    position: absolute;
    left: 40px;
    top: 426px;
    width: 777px;
    height: 348px;
    overflow: hidden;
    background: var(--sand);
  }
  .band-sky {
    position: absolute;
    left: 0; top: 0;
    width: 100%;
    height: 153px;
    background: var(--sky);
  }
  .band-foam {
    position: absolute;
    left: 0; top: 153px;
    width: 100%;
    height: 57px;
    background: var(--foam);
  }
  .brand-name {
    position: absolute;
    left: 186px;
    top: 38px;
    margin: 0;
    font-weight: 800;
    font-size: 38px;
    line-height: 44px;
    letter-spacing: 0.2px;
    text-transform: uppercase;
    white-space: nowrap;
  }
  .brand-name .tm {
    position: relative;
    top: -20px;
    margin-left: 2px;
    font-size: 9px;
    line-height: 0;
    vertical-align: baseline;
  }
  .product-type {
    position: absolute;
    left: 0;
    right: 0;
    top: 166px;
    margin: 0;
    text-align: center;
    font-weight: 500;
    font-size: 22px;
    line-height: 28px;
    letter-spacing: 11px;
    text-indent: 11px;
  }
  .ingredient {
    position: absolute;
    top: 223px;
    width: 160px;
    margin-left: -80px;
    display: flex;
    flex-direction: column;
    align-items: center;
  }
  .ingredient--moss { left: 247px; }
  .ingredient--oats { left: 388px; }
  .ingredient--aloe { left: 530px; }
  .ingredient-icon {
    width: 40px;
    height: 40px;
    border-radius: 8px;
    background: var(--icon-tint);
  }
  .ingredient-name {
    margin-top: 4px;
    font-weight: 500;
    font-size: 25px;
    line-height: 30px;
    white-space: nowrap;
  }
  .net-volume {
    position: absolute;
    left: 0;
    right: 0;
    top: 304px;
    margin: 0;
    text-align: center;
    font-weight: 500;
    font-size: 15px;
    line-height: 20px;
  }
</style>
</head>
<body>
  <section class="label" aria-label="Soothing cream jar label, front side">
    <div class="band-sky"></div>
    <div class="band-foam"></div>

    <h1 class="brand-name">The Pine Grove<br>Soothed My Skin<span class="tm">TM</span></h1>

    <p class="product-type">SOOTHING CREAM</p>

    <div class="ingredient ingredient--moss">
      <span class="ingredient-icon" role="img" aria-label="Line icon of sea moss"></span>
      <span class="ingredient-name">Sea Moss</span>
    </div>
    <div class="ingredient ingredient--oats">
      <span class="ingredient-icon" role="img" aria-label="Line icon of an oat sprig with grains"></span>
      <span class="ingredient-name">Oats</span>
    </div>
    <div class="ingredient ingredient--aloe">
      <span class="ingredient-icon" role="img" aria-label="Line icon of an aloe vera plant"></span>
      <span class="ingredient-name">Aloe Vera</span>
    </div>

    <p class="net-volume">4 fl oz / 118 ml</p>
  </section>
</body>
</html>
```